Formal letterhead for Commercial Real Estate Company

Formal and professional letterhead for the transactional documents of a commercial real estate company.

Elements to be Included between header and footer:

- Logo (attached)(should be applied without the yellow background, in other words, the background colour for the design should be white)
- Slogan: Your Property Solution
- Physical Address: 27 Kestrel Lane, Ferndale, Pinetown, 3610
- Postal Address: PO Box 61894, Windermere, 3615
- Phone: 031 486 9142
- Fax: 031 337 8129
- Website: www.terrabuild.co.zaz
- eMail: contact@terrabuild.co.za

The brand guide is attached (the one you last provided), it does not provide direction on letterhead specifically but on other brand aspects.

Industry/Entity Type

Real Estate

```html
<!DOCTYPE html>
<html lang="en">
<head>
<meta charset="utf-8">
<title>Terra Build Letterhead</title>
<link href="https://fonts.googleapis.com/css2?family=Montserrat:wght@200;300;600&family=Roboto+Condensed:wght@400&display=swap" rel="stylesheet">
<style>
  :root {
    --backdrop: #dedd8c;
    --paper: #ffffff;
    --ink: #111111;
    --brand-yellow: #e6e61c;
    --brand-olive: #a9a915;
    --brand-grey: #b9b9b9;
    --line-grey: #4a4a4a;
    --slogan-grey: #9a9a9a;
    --seal-pale: #fbfbd8;
    --seal-grey: #d2d2d2;
    --contact-ink: #3d3d10;
  }
  html, body {
    margin: 0;
    width: 1200px;
    height: 784px;
    overflow: hidden;
    background: var(--backdrop);
  }
  .letterhead {
    position: absolute;
    left: 340px;
    top: 24px;
    width: 520px;
    height: 736px;
    background: var(--paper);
    box-shadow: 0 6px 18px rgba(80, 80, 20, 0.25);
    overflow: hidden;
  }
  .header-rule {
    position: absolute;
    height: 5px;
  }
  .header-rule--grey {
    left: 34px;
    top: 48px;
    width: 236px;
    background: var(--line-grey);
  }
  .header-rule--yellow {
    left: 432px;
    top: 62px;
    width: 88px;
    background: var(--brand-yellow);
  }
  .brand {
    position: absolute;
    left: 282px;
    top: 38px;
    margin: 0;
    font-family: "Montserrat", sans-serif;
    font-weight: 600;
    font-size: 20px;
    line-height: 24px;
    letter-spacing: 0.5px;
    color: var(--ink);
    white-space: nowrap;
  }
  .seal {
    position: absolute;
    left: 262px;
    top: 556px;
  }
  .footer-wave {
    position: absolute;
    left: 0;
    bottom: 0;
  }
  .slogan {
    position: absolute;
    left: 30px;
    top: 538px;
    margin: 0;
    font-family: "Montserrat", sans-serif;
    font-weight: 200;
    font-size: 22px;
    line-height: 28px;
    color: var(--slogan-grey);
    letter-spacing: 0.5px;
    white-space: nowrap;
  }
  .slogan strong {
    font-weight: 300;
  }
  .contact {
    position: absolute;
    left: 14px;
    top: 646px;
    font-family: "Roboto Condensed", sans-serif;
    font-size: 7.5px;
    line-height: 11px;
    color: var(--contact-ink);
  }
  .contact__icons {
    display: flex;
    align-items: center;
    gap: 4px;
    margin-bottom: 3px;
  }
  .contact__rule {
    width: 34px;
    height: 1px;
    background: var(--contact-ink);
  }
  .contact__dot {
    width: 6px;
    height: 6px;
    border-radius: 50%;
    background: var(--contact-ink);
  }
  .contact p { margin: 0; white-space: nowrap; }
</style>
</head>
<body>
  <main class="letterhead">
    <div class="header-rule header-rule--grey"></div>
    <p class="brand">Terra Build</p>
    <div class="header-rule header-rule--yellow"></div>

    <svg class="seal" width="170" height="170" viewBox="0 0 170 170" aria-hidden="true">
      <circle cx="85" cy="85" r="84" fill="var(--seal-pale)"/>
      <circle cx="85" cy="85" r="58" fill="var(--seal-grey)"/>
    </svg>

    <svg class="footer-wave" width="520" height="150" viewBox="0 586 520 150" aria-hidden="true">
      <path d="M0,620 C120,620 200,650 290,700 C360,735 440,730 520,729 L520,736 L0,736 Z" fill="var(--brand-yellow)"/>
      <path d="M0,607 C125,607 215,640 305,694 L290,700 C200,650 120,620 0,620 Z" fill="var(--brand-grey)"/>
      <path d="M0,600 C130,600 222,634 312,690" fill="none" stroke="var(--brand-olive)" stroke-width="2"/>
    </svg>

    <p class="slogan">Your <strong>PROPERTY</strong> Solution</p>

    <div class="contact">
      <div class="contact__icons">
        <span class="contact__rule"></span>
        <span class="contact__dot"></span>
        <span class="contact__dot"></span>
        <span class="contact__dot"></span>
        <span class="contact__dot"></span>
        <span class="contact__dot"></span>
        <span class="contact__rule"></span>
      </div>
      <p>27 Kestrel Lane, Ferndale, Pinetown, 3610 | PO Box 61894, Windermere, 3615</p>
      <p>031 486 9142 | 031 337 8129 | contact@terrabuild.co.za</p>
      <p>www.terrabuild.co.zaz</p>
    </div>
  </main>
</body>
</html>
```